Upmarket Artwork, Furniture Retailer needs to Improve existing Vendora Product Template Page

We need to improve an existing design for a Vendora product page. For professional quality we will then like to use the same designer for further work e.g vendora store(Web page)
We need a Web Designer for an exciting new online retailer based in Sydney. Our product is upmarket Scandanavian designed indoor furniture and Rattan outdoor furniture and Modernist Artwork.
Existing Banners,Logo, text, and template can be the same but the Graphic Design need improvement to give the Vendora product page an edge. We like the Green and Brown colours. Attached is teh logo and the extsing Product template

Reason: Thank you everyone for sending through your designs. Soem designs have come in late today and we need some extra time to contact designers. We will be in contact with you to let you know how you went. Kind Regards Delphine

Reason: Still waiting on some redesigns. My apologies for the belated reply. Thank you everyone for sending through great quality work.

Reason: My apologies for the delay. We are waiting on a re design to finalise. Thank you everyone for your patience. Cheers Delphine

Target Market(s)

Upmarket house proud 25-55 professionals

Industry/Entity Type

Graphic Design

Requirements
Must have
• To have an edge to Maximise Buyers
Nice to have
• To use the colours Greens and browns

```html
<!DOCTYPE html>
<html lang="en">
<head>
<meta charset="utf-8">
<title>Maison Alder – Product Page</title>
<link rel="stylesheet" href="https://fonts.googleapis.com/css2?family=Cinzel:wght@400;700&family=PT+Serif:wght@400;700&display=swap">
<style>
:root{
  --bg-dark:#2a170b;
  --bg-mid:#4a2812;
  --bg-glow:#6b3a18;
  --orange:#c8661e;
  --orange-light:#e08a3a;
  --green:#6f8f2a;
  --green-dark:#4f6a1a;
  --cream:#f1ede2;
  --cream-line:#d9d2bf;
  --ink:#4a3a2c;
  --ink-soft:#6d5e4f;
  --white:#ffffff;
  --art-a:#c9a468;
  --art-b:#8a6a3e;
  --art-c:#e9d9b4;
}
*{margin:0;padding:0;box-sizing:border-box}
html,body{width:1200px;height:2688px;overflow:hidden}
body{
  position:relative;
  background:radial-gradient(ellipse at 50% 20%,var(--bg-glow) 0%,var(--bg-mid) 35%,var(--bg-dark) 80%);
  font-family:"PT Serif",Georgia,serif;color:var(--ink);
}
.abs{position:absolute}
.brand{left:0;width:1200px;top:52px;text-align:center;font-family:"Cinzel",serif;font-weight:700;font-size:52px;color:var(--cream);letter-spacing:2px}
.brand .dot{display:inline-block;width:14px;height:14px;border-radius:50%;background:var(--green);margin-right:14px;vertical-align:middle}
.main-nav{left:240px;top:148px;width:720px;height:32px;display:flex;background:linear-gradient(var(--orange-light),var(--orange));border-top:1px solid #f2b072}
.main-nav a{flex:1;text-align:center;line-height:32px;font-family:"Cinzel",serif;font-size:14px;color:var(--white);text-decoration:none;border-right:1px solid rgba(0,0,0,.2)}
.main-nav a.active{background:var(--bg-dark)}
.hero{left:160px;top:180px;width:880px;height:428px;background:linear-gradient(110deg,var(--art-b) 0%,var(--art-a) 30%,var(--art-c) 55%,var(--art-a) 75%,var(--art-b) 100%)}
.hero-arrow{top:340px;width:40px;height:90px}
.seal{border-radius:50%}
.hero-seal{left:910px;top:450px;width:120px;height:120px;background:var(--green);border:5px solid var(--white)}
.caption{left:160px;top:608px;width:880px;height:34px;background:linear-gradient(var(--green),var(--green-dark));color:var(--white);font-family:"Cinzel",serif;font-size:14px;line-height:34px;padding:0 18px;display:flex;justify-content:space-between}
.caption b{font-size:16px}
.panel{background:var(--cream);padding:22px 26px;font-size:14px;line-height:1.5;color:var(--ink-soft)}
.info-panel{left:160px;top:660px;width:500px;height:752px}
.info-section{padding-bottom:18px;margin-bottom:18px;border-bottom:1px solid var(--cream-line)}
.info-section:last-child{border:0}
.info-title{display:flex;align-items:center;gap:14px;font-family:"Cinzel",serif;font-size:22px;color:var(--ink);margin-bottom:10px}
.info-title .bullet{width:26px;height:26px;border-radius:50%;background:var(--orange)}
.lead{color:var(--ink);margin-bottom:6px}
.info-section ul{list-style:none}
.info-section li{margin-bottom:4px}
.pdf-btn{display:inline-block;margin-top:12px;background:linear-gradient(var(--orange-light),var(--orange));color:var(--white);font-family:"Cinzel",serif;padding:8px 22px;text-align:center;line-height:1.1}
.pdf-btn small{display:block;font-size:11px}
.pdf-btn span{font-size:22px}
.gallery{left:672px;top:660px;width:368px;display:grid;grid-template-columns:1fr 1fr;gap:10px}
.gallery .shot{height:160px;background:linear-gradient(120deg,var(--art-b),var(--art-a) 45%,var(--art-c) 70%,var(--art-b));border:4px solid var(--cream)}
.band-title{background:linear-gradient(var(--bg-mid),var(--bg-dark));border-bottom:4px solid var(--orange);color:var(--white);font-family:"Cinzel",serif;font-size:22px;padding:10px 22px}
.block{background:var(--cream)}
.block p{padding:0 26px;margin-top:16px;font-size:14px;line-height:1.5;color:var(--ink-soft)}
.warranty{left:160px;top:1440px;width:500px;height:360px}
.delivery{left:160px;top:1820px;width:500px;height:360px}
.payment{left:672px;top:1530px;width:368px;height:230px}
.about{left:672px;top:1780px;width:368px;height:400px}
.stamp{position:absolute;right:24px;bottom:20px;width:100px;height:100px;border-radius:50%;border:4px solid var(--ink);background:var(--cream-line)}
.pay-marks{display:flex;gap:10px;padding:14px 26px}
.pay-marks span{width:56px;height:34px;border-radius:4px;background:var(--cream-line);border:1px solid var(--ink-soft)}
.pay-marks span.wide{width:80px}
.trust{display:flex;gap:20px;padding:14px 26px}
.trust .shield{width:140px;height:80px;border-radius:8px;background:var(--ink)}
.trust .round{width:90px;height:90px;border-radius:50%;background:#1e1e1e}
.range{left:0;top:2240px;width:1200px;height:320px;background:linear-gradient(var(--bg-dark),var(--bg-mid),var(--bg-dark))}
.range-item{position:absolute;top:2262px;width:170px}
.range-item h3{background:linear-gradient(var(--orange-light),var(--orange));color:var(--white);font-family:"Cinzel",serif;font-size:13px;text-align:center;padding:4px 0;font-weight:400}
.range-item .shot{margin-top:8px;height:220px;background:linear-gradient(120deg,var(--art-b),var(--art-a) 45%,var(--art-c) 70%,var(--art-b));border:4px solid var(--cream)}
.range-arrow{top:2380px;width:30px;height:60px}
.footer{left:0;top:2636px;width:1200px;text-align:center;font-size:12px;color:var(--cream-line);letter-spacing:1px}
</style>
</head>
<body>
<div class="abs brand"><span class="dot"></span>Maison Alder</div>

<nav class="abs main-nav">
  <a href="#">Furniture</a><a href="#">Delivery</a><a href="#" class="active">Warranty</a><a href="#">About Us</a><a href="#">Contact Us</a><a href="#">Visit Store</a>
</nav>

<div class="abs hero" role="img" aria-label="Modern oil painting of a metallic landscape on framed canvas"></div>
<svg class="abs hero-arrow" style="left:112px" viewBox="0 0 40 90"><polyline points="34,4 6,45 34,86" fill="none" stroke="#e9d9b4" stroke-width="3"/></svg>
<svg class="abs hero-arrow" style="left:1048px" viewBox="0 0 40 90"><polyline points="6,4 34,45 6,86" fill="none" stroke="#e9d9b4" stroke-width="3"/></svg>
<div class="abs seal hero-seal"></div>

<div class="abs caption"><span>Modern Oil Painting - Metal Evoke Beautiful Landscape, Canvas Framed</span><b>RRP $195</b></div>

<section class="abs panel info-panel">
  <div class="info-section">
    <h2 class="info-title"><span class="bullet"></span>Description</h2>
    <p class="lead">Modern Oil painting – Metal Element to evoke Beautiful Landscape, Canvas – Framed</p>
    <p>Each canvas is painted by hand in a calm studio setting, layering oil colour with metallic leaf to suggest a quiet landscape at dusk. The piece arrives framed and ready to hang, bringing warmth and texture to living rooms, hallways and modern dining spaces.</p>
  </div>
  <div class="info-section">
    <h2 class="info-title"><span class="bullet"></span>Quality Features</h2>
    <ul>
      <li>Oil painting on canvas</li>
      <li>Metal leaf elegantly integrated within thick paint</li>
      <li>Hand painted by individual artists hence no painting ever the same</li>
      <li>Slight variation in image shown</li>
    </ul>
  </div>
  <div class="info-section">
    <h2 class="info-title"><span class="bullet"></span>Package Includes</h2>
    <ul>
      <li>Optional attached wire wrapped around fixture frame</li>
      <li>Ready to display, attachments included</li>
    </ul>
    <div class="pdf-btn"><small>Assembly Instructions</small><span>Download PDF</span></div>
  </div>
  <div class="info-section">
    <h2 class="info-title"><span class="bullet"></span>Dimensions</h2>
    <p>Length 90 cm x Height 90 cm x 4.5 cm Thick</p>
  </div>
</section>

<div class="abs gallery">
  <div class="shot" role="img" aria-label="Painting detail view"></div>
  <div class="shot" role="img" aria-label="Painting detail view"></div>
  <div class="shot" role="img" aria-label="Painting detail view"></div>
  <div class="shot" role="img" aria-label="Painting detail view"></div>
  <div class="shot" role="img" aria-label="Painting detail view"></div>
  <div class="shot" role="img" aria-label="Painting detail view"></div>
  <div class="shot" role="img" aria-label="Painting detail view"></div>
  <div class="shot" role="img" aria-label="Painting detail view"></div>
  <div class="shot" role="img" aria-label="Painting detail view"></div>
  <div class="shot" role="img" aria-label="Painting detail view"></div>
</div>

<section class="abs block warranty">
  <h2 class="band-title">Warranty</h2>
  <p>Every piece we sell is covered by our twelve month warranty against faults in materials and workmanship. Should anything arrive damaged, simply let us know within seven days and we will arrange a replacement or full refund.</p>
  <p>Our team inspects each artwork and furniture item before dispatch, and every parcel is packed with care. Please keep your original packaging until you are happy with your purchase, as it helps us process any claim quickly.</p>
  <div class="stamp"></div>
</section>

<section class="abs block delivery">
  <h2 class="band-title">Delivery</h2>
  <p>We deliver Australia wide using trusted freight partners. Orders are dispatched within two business days and you will receive tracking details by message as soon as your item is on its way.</p>
  <p>Larger furniture items are delivered to your door by a two person team. Remote areas may take a little longer, and we will contact you to arrange a suitable time.</p>
  <div class="stamp"></div>
</section>

<section class="abs block payment">
  <h2 class="band-title">Payment</h2>
  <p>We accept secure payment through the main online wallets and all major credit cards. Payment is due within three days of purchase so your order can be dispatched promptly.</p>
  <div class="pay-marks"><span class="wide"></span><span></span><span></span><span></span></div>
</section>

<section class="abs block about">
  <h2 class="band-title">About Us</h2>
  <p>We are an online retailer based in Sydney offering upmarket Scandinavian indoor furniture, rattan outdoor furniture and modernist artwork. Our collection is chosen for quality, comfort and lasting style.</p>
  <p>We work closely with makers and artists to bring considered design into your home, with friendly service from the first question right through to delivery at your door.</p>
  <div class="trust"><div class="shield"></div><div class="round"></div></div>
</section>

<div class="abs range"></div>
<svg class="abs range-arrow" style="left:160px" viewBox="0 0 30 60"><polyline points="26,4 4,30 26,56" fill="none" stroke="#e9d9b4" stroke-width="3"/></svg>
<svg class="abs range-arrow" style="left:1010px" viewBox="0 0 30 60"><polyline points="4,4 26,30 4,56" fill="none" stroke="#e9d9b4" stroke-width="3"/></svg>
<div class="range-item" style="left:215px"><h3>Indoor Furniture</h3><div class="shot" role="img" aria-label="Indoor furniture artwork preview"></div></div>
<div class="range-item" style="left:410px"><h3>Outdoor Furniture</h3><div class="shot" role="img" aria-label="Outdoor furniture artwork preview"></div></div>
<div class="range-item" style="left:605px"><h3>Artwork</h3><div class="shot" role="img" aria-label="Artwork preview"></div></div>
<div class="range-item" style="left:800px"><h3>Specials</h3><div class="shot" role="img" aria-label="Specials artwork preview"></div></div>

<div class="abs footer">Copyright © 2024 Maison Alder. All rights reserved. Prices include GST.</div>
</body>
</html>
```